STYLISH

It will be a brochure that exemplifies a project to make a modern and avant-garde LEGAL MAGAZINE to "sell it" to the sponsors, it will be a legal niche magazine for lawyers. The style is of the type "The Velvet Drum" of the lawyers, breaks scheme, more disruptive More alternative with innovative personality and that calls the attention. It will be a collection magazine, to look at the reception of the Legal Firms. For public between 27 and 45 years. The name of the Magazine will be EL VERGEL

Target Market(s)

Chilean Lawyers between 27 and 45 years old.

Industry/Entity Type

Legal

Logo Text

EL VERGEL

Font styles to use
Sans Serif

Colors

Designer to choose colors to be used in the design.

Requirements
Must have
• Must say the name of the Magazine EL VERGEL Elevate the lawyer by giving him a different "coolness". We make them look and feel cool Elevate the lawyer to a public figure. They have something important to say. Our covers reflect that. A lawyer's study in a rich, unique session. The lawyer should be at the center of all our sections. They always in the middle. They are our protagonists.
Nice to have
• Minimalist, cool, fine. 1. With the white border like MORDANTE MAGAZINE attached. 2. The cover must have the photograph with the pictures of the opposite attached .. 3. Name ok the magazine: THE GROVE 4. On the left footer the word: COLLECTION | 01 5. On the write footer: THE MOST PRESTIGIOUS ATTORNEY ACCORDING TO HALLORAN & BRECK
Should not have
• information saturation

```html
<!DOCTYPE html>
<html lang="es">
<head>
<meta charset="UTF-8">
<title>El Vergel — Colección 01</title>
<link rel="stylesheet" href="https://fonts.googleapis.com/css2?family=Montserrat:wght@300;400;600&display=swap">
<style>
  :root {
    --page-bg: #e9e9e7;
    --photo-deep: #152226;
    --photo-dark: #22363a;
    --photo-mid: #3f5e60;
    --photo-light: #8a9c98;
    --photo-suit: #4a5354;
    --ink-white: #ffffff;
    --title-white: rgba(255, 255, 255, 0.82);
  }
  * { margin: 0; padding: 0; box-sizing: border-box; }
  html, body {
    width: 681px;
    height: 1200px;
    overflow: hidden;
    background: var(--page-bg);
    font-family: "Montserrat", sans-serif;
  }
  .canvas {
    position: relative;
    width: 681px;
    height: 1200px;
    display: flex;
    align-items: center;
    justify-content: center;
  }
  .cover {
    position: relative;
    width: 560px;
    height: 733px;
    overflow: hidden;
    box-shadow: 0 10px 30px rgba(0, 0, 0, 0.18);
  }
  .cover-photo {
    position: absolute;
    inset: 0;
    background:
      radial-gradient(ellipse 32% 70% at 55% 62%, rgba(74, 83, 84, 0.85) 0%, rgba(74, 83, 84, 0.35) 55%, rgba(74, 83, 84, 0) 100%),
      linear-gradient(150deg, rgba(138, 156, 152, 0.75) 0%, rgba(138, 156, 152, 0.15) 30%, rgba(21, 34, 38, 0) 55%, rgba(21, 34, 38, 0.75) 100%),
      linear-gradient(90deg, var(--photo-dark) 0%, var(--photo-mid) 22%, var(--photo-light) 40%, var(--photo-mid) 62%, var(--photo-dark) 82%, var(--photo-deep) 100%);
  }
  .cover-frame {
    position: absolute;
    top: 24px;
    left: 18px;
    right: 18px;
    bottom: 22px;
    border: 2px solid var(--ink-white);
  }
  .masthead {
    position: absolute;
    top: 318px;
    left: 64px;
    color: var(--title-white);
    font-size: 72px;
    letter-spacing: 2px;
    line-height: 1;
    white-space: nowrap;
  }
  .masthead-light { font-weight: 300; }
  .masthead-bold { font-weight: 600; }
  .footer-issue {
    position: absolute;
    left: 48px;
    bottom: 62px;
    color: var(--ink-white);
    font-weight: 300;
    font-size: 16px;
    letter-spacing: 1px;
  }
  .footer-tagline {
    position: absolute;
    right: 48px;
    bottom: 56px;
    color: var(--ink-white);
    font-weight: 600;
    font-size: 10.5px;
    line-height: 1.45;
    letter-spacing: 0.4px;
    text-align: left;
  }
</style>
</head>
<body>
  <main class="canvas">
    <article class="cover">
      <div class="cover-photo" role="img" aria-label="Photograph of a lawyer in a grey suit seen from below, standing at the centre among tall glass office towers, in teal and grey tones"></div>
      <div class="cover-frame"></div>
      <h1 class="masthead"><span class="masthead-light">EL</span> <span class="masthead-bold">VERGEL</span></h1>
      <p class="footer-issue">COLECCIÓN | 01</p>
      <p class="footer-tagline">EL ABOGADO MÁS PRESTIGIOSO<br>SEGÚN HALLORAN &amp; BRECK</p>
    </article>
  </main>
</body>
</html>
```